依頼概要
■ 依頼の目的/概要

弊社は「カード選びナビ広場 http://www.hoshizora-cardnavi.com/ 」というクレジットカードの比較サイトを運営しています。
今回はこのカード選びナビ広場のトップページのサイトデザインリニューアルをお願いします。

現在、サイト内( http://www.hoshizora-cardnavi.com/ )にある素材は自由に使って頂いて構いません。
既存のデザインを残しつつデザインをしていただいても
逆に完全新規にデザインをしていただいても構いません。
最終的なクオリティが高ければOKです。
素材サイトで何か素材を購入すればよりクオリティが高くなるのであれば
別途素材の購入も検討します。
その際はメッセージでご連絡ください。

■コーディング不要
コーディングは不要なので、デザインのみでOKです。

■ 希望するウェブデザイン

サイト訪問者が楽しくクレジットカードを選んだり
クレジットカードについての知識を学んだりできるようなデザインが希望です。
逆にサイト訪問者が堅苦しく感じてしまうようなデザインは避けたいです。
既存サイトでは下記URLのようなサイトデザインが好みです。

http://www.mz.tobira-net.com/mobile/index.html?bid=mz_gn_0007
http://www.mirumart.co.jp/kuruma/index.html?ca=top_glo_009
http://store.fenlow.com/jp/
http://store.tavix.jp/Special/Compare/Computer/Relmo/index.html

また「クレジットカード」で検索して1ページ目に出てくるサイトには
綺麗なサイトが多いので、こちらも参考にして頂きたいです。

【サイズの横幅について】

現在の横幅はぴったり950pxですが、
980px前後までであれば、横幅が大きくなっても構いません。
横幅が現在よりも小さくなるのは不可です。

ただし、ヘッダー部分とフッター部分は下記サイトのように横全体に広がっているデザインが希望です。
http://www.qrt.co.jp/ordercard/index.html

■ 納品ファイルの希望

第一希望 フォトショップ形式 + BMP形式
第二希望 イラストレーター形式 + BMP形式

■ 進め方

弊社の希望するイメージに近い提案を1つ(場合によって複数)選択させて頂きます。希望に近づけるために、修正要望を個別にさせて頂くこともあります。コンペ方式のため、修正後に当選されない場合も、どうかご了承ください。

■ その他/注意点

選択させて頂いたウェブデザインの著作権(財産権)等の扱いはTezukuri利用規約に従い、弊社に譲渡をお願いします。フォントや画像素材などを利用する場合は上記利用用途に使用できることを確認し、第三者の知的財産権等に注意して下さい。
■リニューアルによる変更点
今回のリニューアルではデザイン面だけでなくシステム面も強化するため
トップページのデザインが一部変更になります。
変更点は添付ファイルにまとめました。
なので現在のトップページのデザイン( http://www.hoshizora-cardnavi.com/
ではなく添付ファイル内のデザインを元にデザインをしてください。

```html
<!DOCTYPE html>
<html lang="ja">
<head>
<meta charset="utf-8">
<title>カード選びナビ広場</title>
<link href="https://fonts.googleapis.com/css2?family=Noto+Sans+JP:wght@400;700&display=swap" rel="stylesheet">
<style>
:root{
  --blue:#2f64b7;
  --blue-dark:#1d3f7a;
  --blue-light:#e9f1fb;
  --blue-line:#b9cde9;
  --navy:#20325c;
  --orange:#ef7d12;
  --orange-light:#fdf0e2;
  --red:#d9272e;
  --yellow:#f5c400;
  --text:#333;
  --muted:#777;
  --bg:#f4f6f9;
  --card-silver:#c9d3de;
  --card-gold:#d8b458;
}
*{box-sizing:border-box;margin:0;padding:0}
html,body{width:1200px;height:3332px;overflow:hidden}
body{font-family:"Noto Sans JP",sans-serif;color:var(--text);font-size:13px;background:#fff;line-height:1.5}
.wrap{width:950px;margin:0 auto;position:relative}

/* header */
.site-header{height:96px;background:linear-gradient(#fff,#eef3fa);border-bottom:1px solid var(--blue-line)}
.site-header .wrap{display:flex;align-items:center;height:96px;gap:40px}
.brand{display:flex;align-items:center;gap:10px;font-weight:700;font-size:24px;color:var(--blue)}
.brand-mark{width:22px;height:22px;background:var(--orange)}
.tagline{font-size:18px;color:var(--navy)}
.tagline em{font-style:normal;color:var(--red);font-weight:700}
.util{position:absolute;right:0;top:8px;font-size:11px;color:var(--muted)}
.global-nav{height:50px;background:var(--blue-light);border-bottom:2px solid var(--blue)}
.global-nav ul{list-style:none;display:flex;height:50px;align-items:center;gap:10px}
.global-nav li{flex:1;height:34px;background:#fff;border:1px solid var(--blue-line);border-radius:4px;display:flex;align-items:center;justify-content:center;font-size:13px;color:var(--blue-dark)}
.global-nav li::before{content:"▶";color:var(--orange);font-size:9px;margin-right:6px}

/* intro */
.intro{display:flex;gap:24px;margin-top:18px;height:104px;align-items:center}
.mascot{width:90px;height:96px;background:linear-gradient(#dfe7f2,#b7c6db);border-radius:8px}
.bubble{flex:1;border:2px solid var(--blue-line);border-radius:14px;padding:14px 20px;font-size:13px;background:#fff}
.bubble strong{color:var(--red)}

/* news */
.news{margin-top:14px;border:1px solid var(--blue-line);height:186px}
.news-head{height:38px;background:var(--navy);color:var(--yellow);font-weight:700;font-size:20px;padding-left:20px;line-height:38px;letter-spacing:1px}
.news ul{list-style:none;padding:10px 20px}
.news li{font-size:12px;line-height:23px;border-bottom:1px dotted #ccc}
.news li span{color:var(--blue);margin-right:14px}

/* columns */
.columns{display:flex;gap:20px;margin-top:20px}
.main{width:640px}
.side{width:290px}
.sec{margin-bottom:20px;border:1px solid var(--blue-line);background:#fff}
.sec-head{height:36px;background:linear-gradient(var(--blue),var(--blue-dark));color:#fff;font-weight:700;font-size:15px;line-height:36px;padding-left:16px}
.sec-head::before{content:"●";color:var(--yellow);margin-right:8px;font-size:11px}
.sub-head{margin:12px 14px 6px;padding:4px 10px;border-left:5px solid var(--orange);background:var(--bg);font-weight:700;font-size:13px}

.card-img{background:linear-gradient(135deg,#e6ecf3,var(--card-silver));border-radius:6px}
.card-img.gold{background:linear-gradient(135deg,#f2dfa4,var(--card-gold))}
.card-img.blue{background:linear-gradient(135deg,#a9c4ea,#3f6fb6)}

/* ranking */
.rank-item{display:flex;gap:16px;padding:14px;border-bottom:1px dashed var(--blue-line);height:98px}
.rank-item .card-img{width:120px;height:70px;flex:none}
.rank-title{color:var(--orange);font-weight:700;font-size:14px}
.rank-title b{color:var(--red);margin-right:6px}
.rank-desc{font-size:11.5px;color:var(--muted)}
.rank-link{font-size:11px;color:var(--blue)}

.banners{display:flex;gap:10px;margin-bottom:20px;height:92px}
.banners div{flex:1;border:1px solid var(--blue-line);background:linear-gradient(90deg,#dfeaf8,#f7fafd)}

/* purpose tiles */
.tiles{display:grid;grid-template-columns:repeat(5,1fr);gap:12px;padding:6px 14px 14px}
.tile{font-size:11px;text-align:center;color:var(--blue-dark)}
.tile .ph{height:82px;border:1px solid var(--blue-line);margin-bottom:4px;background:linear-gradient(#e7eef8,#c9d8ec)}

/* search form */
.filter{padding:6px 14px 14px}
.fgroup{margin-top:10px}
.fgroup h4{font-size:12px;color:var(--blue-dark);border-bottom:1px solid var(--blue-line);padding-bottom:3px;margin-bottom:6px}
.checks{display:grid;grid-template-columns:repeat(4,1fr);row-gap:5px;font-size:11.5px}
.checks span::before{content:"";display:inline-block;width:11px;height:11px;border:1px solid #999;margin-right:5px;vertical-align:-1px;background:#fff}
.select{display:inline-block;width:180px;height:22px;border:1px solid #aaa;font-size:11px;padding:2px 6px;background:#fff}
.search-bar{display:flex;align-items:center;justify-content:center;gap:16px;margin-top:18px;padding:12px;background:var(--orange-light);border:1px solid #f3c89a;font-size:12px}
.search-bar b{color:var(--red);font-size:18px}
.btn{display:inline-block;background:linear-gradient(#f99a3a,var(--orange));color:#fff;font-weight:700;border-radius:4px;padding:6px 22px;font-size:13px}

/* list */
.listgrid{display:grid;grid-template-columns:1fr 1fr;gap:12px;padding:12px}
.lbox{border:1px solid var(--blue-line);height:150px}
.lbox h5{background:var(--blue-light);font-size:12px;color:var(--blue-dark);padding:4px 10px}
.lbox .row{display:flex;gap:6px;padding:8px}
.lbox .row .card-img{flex:1;height:52px}
.lbox .btn{margin:4px auto;display:block;width:120px;text-align:center;padding:5px 0}

/* side */
.side-banner{height:150px;margin-bottom:14px;background:linear-gradient(135deg,#1d2a44,#4a5c80);border-radius:4px}
.menu{border:1px solid var(--blue-line);margin-bottom:14px}
.menu h3{background:var(--orange);color:#fff;font-size:13px;padding:6px 10px}
.menu ul{list-style:none;padding:6px 10px}
.menu li{font-size:12px;line-height:28px;border-bottom:1px dotted #ccc}
.menu li::before{content:"›";color:var(--orange);margin-right:6px;font-weight:700}
.brands{display:grid;grid-template-columns:repeat(3,1fr);gap:8px;margin-bottom:14px}
.brands div{height:44px;border:1px solid #ddd;display:flex;align-items:center;justify-content:center;font-size:11px;font-weight:700;color:var(--blue-dark)}
.ad{height:260px;margin-bottom:14px;background:linear-gradient(#f7eed5,#e3c781);border:1px solid #d6b86b}
.pick{border:1px solid var(--blue-line);margin-bottom:14px}
.pick h3{background:linear-gradient(var(--blue),var(--blue-dark));color:#fff;font-size:13px;padding:6px 10px}
.pick-item{display:flex;gap:10px;padding:10px;border-bottom:1px dashed var(--blue-line);height:160px}
.pick-item .card-img{width:96px;height:60px;flex:none}
.pick-item p{font-size:11px;color:var(--muted)}
.pick-item strong{display:block;color:var(--orange);font-size:12px}
.side-bottom{height:120px;background:linear-gradient(#fbe2c4,#f3a85b);border-radius:4px}

/* footer */
.site-footer{position:absolute;left:0;top:2940px;width:1200px;height:392px;background:var(--bg);border-top:3px solid var(--blue)}
.about{padding:24px 0 18px;font-size:12px;color:#555;border-bottom:1px solid #ddd}
.about h4{font-size:13px;margin-bottom:6px;color:var(--blue-dark)}
.footer-links{text-align:center;font-size:12px;color:var(--blue);padding:18px 0}
.copy{text-align:center;font-size:11px;color:var(--muted);background:var(--navy);color:#cfd7e6;padding:10px 0;position:absolute;bottom:0;width:100%}
</style>
</head>
<body>
<header class="site-header">
  <div class="wrap">
    <div class="brand"><span class="brand-mark"></span>カード選びナビ広場</div>
    <p class="tagline">ライフスタイルに合ったお<em>得なクレジットカード</em>を選ぼう!</p>
    <p class="util">サイトマップ | お問い合わせ</p>
  </div>
</header>
<nav class="global-nav">
  <div class="wrap">
    <ul><li>カードの基本</li><li>目的で選ぶ比較表</li><li>人気ランキング</li><li>ヘルプ</li><li>カード一覧</li></ul>
  </div>
</nav>

<div class="wrap">
  <section class="intro">
    <div class="mascot" role="img" aria-label="サイトの案内役キャラクター"></div>
    <p class="bubble">クレジットカード選びでお悩みのあなたへ。年会費やポイント還元率などを比べて、<strong>自分にぴったりの一枚</strong>を見つけましょう。初めての方も気軽にどうぞ。</p>
  </section>

  <section class="news">
    <h2 class="news-head">What's New</h2>
    <ul>
      <li><span>2013.05.20</span>おすすめカードのランキングを更新しました</li>
      <li><span>2013.05.14</span>ポイント比較ページに新しいカードを追加しました</li>
      <li><span>2013.05.08</span>旅行保険の特集記事を公開しました</li>
      <li><span>2013.04.30</span>年会費無料カードの一覧を見直しました</li>
      <li><span>2013.04.22</span>ゴールドカード比較表を更新しました</li>
      <li><span>2013.04.15</span>サイトデザインをリニューアルしました</li>
    </ul>
  </section>

  <div class="columns">
    <main class="main">
      <section class="sec">
        <h2 class="sec-head">年会費無料の人気クレジットカード</h2>
        <div class="rank-item"><div class="card-img blue" role="img" aria-label="カード券面"></div><div><p class="rank-title"><b>1位</b>年会費永年無料</p><p class="rank-desc">ポイント還元率が高く、日常の買い物でお得に使える定番カードです。</p><p class="rank-link">詳細を見る ›</p></div></div>
        <div class="rank-item"><div class="card-img" role="img" aria-label="カード券面"></div><div><p class="rank-title"><b>2位</b>入会で最大5,000円相当</p><p class="rank-desc">ネット通販でポイントが貯まりやすく、初めての一枚にもおすすめ。</p><p class="rank-link">詳細を見る ›</p></div></div>
        <div class="rank-item"><div class="card-img" role="img" aria-label="カード券面"></div><div><p class="rank-title"><b>3位</b>最短即日発行</p><p class="rank-desc">急いでカードが欲しい方に。電子マネーとの連携も充実しています。</p><p class="rank-link">詳細を見る ›</p></div></div>
        <div class="rank-item" style="border:0"><div class="card-img blue" role="img" aria-label="カード券面"></div><div><p class="rank-title"><b>4位</b>旅行保険が自動付帯</p><p class="rank-desc">海外旅行によく行く方向けの、保険とサービスが手厚いカードです。</p><p class="rank-link">詳細を見る ›</p></div></div>
      </section>

      <div class="banners">
        <div role="img" aria-label="特集バナー"></div>
        <div role="img" aria-label="キャンペーンバナー"></div>
      </div>

      <section class="sec">
        <h2 class="sec-head">クレジットカードを目的別で探す</h2>
        <h3 class="sub-head">目的別おすすめランキング</h3>
        <div class="tiles">
          <div class="tile"><div class="ph" role="img" aria-label="目的別イメージ"></div>初めてのカード</div>
          <div class="tile"><div class="ph" role="img" aria-label="目的別イメージ"></div>ポイント重視</div>
          <div class="tile"><div class="ph" role="img" aria-label="目的別イメージ"></div>年会費無料</div>
          <div class="tile"><div class="ph" role="img" aria-label="目的別イメージ"></div>マイルを貯める</div>
          <div class="tile"><div class="ph" role="img" aria-label="目的別イメージ"></div>即日発行</div>
          <div class="tile"><div class="ph" role="img" aria-label="目的別イメージ"></div>海外旅行</div>
          <div class="tile"><div class="ph" role="img" aria-label="目的別イメージ"></div>学生向け</div>
          <div class="tile"><div class="ph" role="img" aria-label="目的別イメージ"></div>ネット通販</div>
          <div class="tile"><div class="ph" role="img" aria-label="目的別イメージ"></div>セキュリティ</div>
          <div class="tile"><div class="ph" role="img" aria-label="目的別イメージ"></div>ゴールド</div>
        </div>
      </section>

      <section class="sec">
        <h2 class="sec-head">クレジットカードを条件から絞り込んで探す</h2>
        <div class="filter">
          <div class="fgroup"><h4>カードの種類</h4><div class="checks"><span>一般カード</span><span>ゴールドカード</span><span>プラチナカード</span><span>学生カード</span><span>法人カード</span><span>提携カード</span><span>女性向けカード</span><span>家族カード</span></div></div>
          <div class="fgroup"><h4>年会費</h4><div class="checks"><span>永年無料</span><span>初年度無料</span><span>条件付き無料</span><span>5,000円以下</span><span>10,000円以下</span><span>10,000円以上</span></div></div>
          <div class="fgroup"><h4>ポイント・マイル</h4><div class="checks"><span>還元率1%以上</span><span>マイル移行可</span><span>有効期限なし</span><span>ネット加算</span><span>店舗優待</span><span>誕生月特典</span><span>ボーナス月</span><span>交換先が豊富</span></div></div>
          <div class="fgroup"><h4>付帯保険・サービス</h4><div class="checks"><span>海外旅行保険</span><span>国内旅行保険</span><span>ショッピング保険</span><span>空港ラウンジ</span><span>ロードサービス</span><span>コンシェルジュ</span><span>不正利用補償</span><span>家族特約</span></div></div>
          <div class="fgroup"><h4>国際ブランド</h4><div class="checks"><span>ルミナ</span><span>ステラ</span><span>ヒカリカード</span><span>オルビスカード</span><span>ダイナ</span><span>その他</span></div></div>
          <div class="fgroup"><h4>発行スピード</h4><div class="checks"><span>即日発行</span><span>3営業日以内</span><span>1週間以内</span><span>指定なし</span></div></div>
          <div class="fgroup"><h4>電子マネー</h4><div class="checks"><span>交通系</span><span>後払い型</span><span>チャージ型</span><span>スマホ対応</span><span>オートチャージ</span><span>ポイント二重取り</span></div></div>
          <div class="fgroup"><h4>申込資格・その他</h4><div class="checks"><span>18歳以上</span><span>学生可</span><span>主婦可</span><span>パート可</span><span>ETCカード</span><span>分割払い</span><span>リボ払い</span><span>キャッシング</span></div></div>
          <div class="fgroup"><h4>並び順</h4><span class="select">人気順 ▼</span></div>
          <div class="fgroup"><h4>表示件数</h4><span class="select">20件 ▼</span></div>
          <div class="fgroup"><h4>発行会社</h4><div class="checks"><span>銀行系</span><span>信販系</span><span>流通系</span><span>交通系</span></div></div>
          <div class="search-bar">該当するカード <b>52</b> 件 <span class="btn">この条件で検索</span></div>
        </div>
      </section>

      <section class="sec">
        <h2 class="sec-head">クレジットカード一覧</h2>
        <div class="listgrid">
          <div class="lbox"><h5>スタンダードカード比較</h5><div class="row"><div class="card-img"></div><div class="card-img blue"></div><div class="card-img"></div></div><span class="btn">比較する</span></div>
          <div class="lbox"><h5>マイルが貯まるカード比較</h5><div class="row"><div class="card-img blue"></div><div class="card-img"></div><div class="card-img blue"></div></div><span class="btn">比較する</span></div>
          <div class="lbox"><h5>ゴールドカード比較</h5><div class="row"><div class="card-img gold"></div><div class="card-img gold"></div><div class="card-img gold"></div></div><span class="btn">比較する</span></div>
          <div class="lbox"><h5>ポイント重視カード比較</h5><div class="row"><div class="card-img"></div><div class="card-img gold"></div><div class="card-img blue"></div></div><span class="btn">比較する</span></div>
        </div>
      </section>
    </main>

    <aside class="side">
      <div class="side-banner" role="img" aria-label="プラチナカード紹介バナー"></div>
      <div class="menu">
        <h3>クレジットカードの基礎知識</h3>
        <ul><li>カードの仕組み</li><li>年会費について</li><li>ポイントの貯め方</li><li>審査のポイント</li><li>付帯保険の基本</li><li>よくある質問</li><li>用語集</li></ul>
      </div>
      <div class="brands"><div>ルミナ</div><div>ステラ</div><div>ヒカリ</div><div>オルビス</div><div>ダイナ</div><div>その他</div></div>
      <div class="ad" role="img" aria-label="ゴールドカード広告"></div>
      <div class="pick">
        <h3>おすすめクレジットカード</h3>
        <div class="pick-item"><div class="card-img blue"></div><p><strong>ネットで貯まる</strong>通販でポイント最大3倍。年会費無料で使いやすい一枚。</p></div>
        <div class="pick-item"><div class="card-img"></div><p><strong>旅行に強い</strong>海外旅行保険が自動付帯。空港サービスも充実。</p></div>
        <div class="pick-item"><div class="card-img gold"></div><p><strong>ゴールドの特典</strong>ラウンジ利用や手厚い補償が魅力のカード。</p></div>
        <div class="pick-item"><div class="card-img"></div><p><strong>学生にも人気</strong>申込みが簡単で、はじめての方でも安心です。</p></div>
        <div class="pick-item"><div class="card-img blue"></div><p><strong>即日発行</strong>最短当日に受け取れるスピード発行カード。</p></div>
        <div class="pick-item" style="border:0"><div class="card-img gold"></div><p><strong>還元率が高い</strong>毎日の買い物で着実にポイントが貯まります。</p></div>
      </div>
      <div class="side-bottom" role="img" aria-label="入会キャンペーンバナー"></div>
    </aside>
  </div>
</div>

<footer class="site-footer">
  <div class="wrap">
    <div class="about">
      <h4>カード選びナビ広場とは</h4>
      <p>カード選びナビ広場は、年会費・ポイント・付帯保険などの条件から、あなたに合ったクレジットカードを比較して選べるサイトです。初めての方にも分かりやすく、カードの基礎知識もまとめています。掲載情報は各社の公式発表をもとに定期的に更新しています。お申し込みの際は必ず公式サイトで最新の条件をご確認ください。</p>
    </div>
    <p class="footer-links">運営会社 | お問い合わせ | 広告掲載について | プライバシーポリシー | サイトマップ</p>
  </div>
  <p class="copy">Copyright © 2013 カード選びナビ広場 All Rights Reserved.</p>
</footer>
</body>
</html>
```